Simple elegant business card

General card for a fin and television director.
Just want name, email, phone and address.

Target Market(s)

Prospective employers

Industry/Entity Type

Business

Requirements
Must have
• As above
Nice to have
• Logo but not necessary.
Should not have
• Not too colourful or funky.
• Simplicity and elegance the way to go.

```html
<!DOCTYPE html>
<html lang="en">
<head>
<meta charset="utf-8">
<title>Nora Hale – Business Card</title>
<link href="https://fonts.googleapis.com/css2?family=Quicksand:wght@400&family=Cutive+Mono&display=swap" rel="stylesheet">
<style>
  :root {
    --backdrop: #e9e7e3;
    --card: #f7f7f6;
    --card-edge: #e2e2e0;
    --ink: #1c1c1c;
    --ink-soft: #555555;
    --rule: #9a9a9a;
  }
  * { margin: 0; padding: 0; box-sizing: border-box; }
  html, body {
    width: 1200px; height: 1000px; overflow: hidden;
    background: var(--backdrop);
  }
  .stage {
    width: 1200px; height: 1000px;
    display: flex; align-items: center; justify-content: center;
  }
  .card {
    position: relative;
    width: 440px; height: 740px;
    background: linear-gradient(160deg, #ffffff 0%, var(--card) 55%, #efefee 100%);
    border: 1px solid var(--card-edge);
    box-shadow: 0 10px 30px rgba(0,0,0,0.12);
  }
  .brand {
    position: absolute; top: 110px; left: 50%;
    width: 290px; height: 290px; margin-left: -145px;
    border: 2px solid var(--ink-soft);
    border-radius: 50%;
    display: flex; flex-direction: column; align-items: center; justify-content: center;
  }
  .brand-name {
    font-family: "Quicksand", sans-serif;
    font-weight: 400;
    color: var(--ink);
    font-size: 58px;
    line-height: 1;
    letter-spacing: 4px;
    text-align: center;
    text-transform: uppercase;
  }
  .role {
    position: absolute; top: 500px; left: 0; right: 0;
    text-align: center;
    font-family: "Cutive Mono", monospace;
    font-size: 22px;
    letter-spacing: 4px;
    color: var(--ink);
  }
  .divider {
    position: absolute; top: 548px; left: 90px; right: 90px;
    display: flex; align-items: center; gap: 8px;
  }
  .divider-line { flex: 1; height: 1px; background: var(--rule); }
  .divider-ornament {
    width: 40px; height: 14px; border-radius: 7px;
    background: linear-gradient(90deg, #d6d6d6, #bdbdbd, #d6d6d6);
  }
  .contact {
    position: absolute; top: 590px; left: 75px;
    list-style: none;
    font-family: "Quicksand", sans-serif;
    font-size: 22px;
    letter-spacing: 3px;
    color: var(--ink);
  }
  .contact-item { display: flex; align-items: center; gap: 16px; height: 36px; }
  .contact-icon { width: 18px; height: 18px; flex: none; fill: var(--ink); }
</style>
</head>
<body>
<main class="stage">
  <article class="card">
    <div class="brand">
      <p class="brand-name">Nora<br>Hale</p>
    </div>

    <p class="role">film &amp; tv director</p>

    <div class="divider">
      <span class="divider-line"></span>
      <span class="divider-ornament" role="img" aria-label="small decorative flourish"></span>
      <span class="divider-line"></span>
    </div>

    <ul class="contact">
      <li class="contact-item">
        <svg class="contact-icon" viewBox="0 0 24 24" aria-hidden="true">
          <path d="M6.6 10.8a15 15 0 0 0 6.6 6.6l2.2-2.2a1 1 0 0 1 1-.25 11.4 11.4 0 0 0 3.6.6 1 1 0 0 1 1 1V20a1 1 0 0 1-1 1A17 17 0 0 1 3 4a1 1 0 0 1 1-1h3.5a1 1 0 0 1 1 1c0 1.25.2 2.45.6 3.6a1 1 0 0 1-.25 1z"/>
        </svg>
        <span>+1 310 555 0148</span>
      </li>
      <li class="contact-item">
        <svg class="contact-icon" viewBox="0 0 24 24" aria-hidden="true">
          <path d="M2 5h20v14H2z M3.5 6.5 12 13l8.5-6.5" fill="none" stroke="#1c1c1c" stroke-width="0"/>
          <path d="M2 5h20v2l-10 7L2 7z M2 9l10 7 10-7v10H2z"/>
        </svg>
        <span>norahale@mail.com</span>
      </li>
    </ul>
  </article>
</main>
</body>
</html>
```